New business card for a regional office of a US M&A company

We need business card for a finance company, office based in Hong Kong , our Head office is in US, our business is to Merge and acquires companies , the new office will be a regional office for the Asia Pacific region. We want to use the head office logo as attached ( but don't have to be exactly the same, can be a variation to it) as a base and then add Asia Pacific alongside the logo.
We would prefer to have be bilingual Eng + Chinese, although we don't really have Chinese company name .

Industry/Entity Type

Business

Contact Information for Business Card

Carla Beth Soren
 

VP,
APAC M&A Operations
TOVAR CREST Asia Pacific Limited
 
Unit 1407, K82
27 Sai Lok Fung Road, 
Hong Kong 
 
M: +852 6481 2037
T : +852 2736 4100
F : +852 2736 4155
VOIP: 4813
 
cbsoren@tovarcrest.com

Font styles to use
Serif
Sans Serif

Colors

Designer to choose colors to be used in the design.

Requirements
Must have
• APAC Office

```html
<!DOCTYPE html>
<html lang="en">
<head>
<meta charset="utf-8">
<title>Tovar Crest APAC Business Card</title>
<link href="https://fonts.googleapis.com/css2?family=Lato:wght@400;700;900&display=swap" rel="stylesheet">
<style>
  :root {
    --navy: #12365a;
    --navy-deep: #0c2642;
    --cyan: #2bb8dc;
    --white: #ffffff;
    --paper: #f3f4f6;
    --stage: #2b2d30;
  }
  * { box-sizing: border-box; margin: 0; padding: 0; }
  html, body { width: 1200px; height: 1031px; overflow: hidden; }
  body {
    background: var(--stage);
    font-family: "Lato", sans-serif;
    display: flex; flex-direction: column; align-items: center; justify-content: center;
    gap: 44px;
  }
  .card {
    width: 800px; height: 457px; border-radius: 26px; overflow: hidden; position: relative;
    box-shadow: 0 14px 40px rgba(0,0,0,.45);
  }
  /* Front */
  .card-front {
    background: linear-gradient(145deg, #184170 0%, var(--navy) 45%, var(--navy-deep) 100%);
  }
  .map-texture {
    position: absolute; inset: 40px 60px;
    background: radial-gradient(ellipse at 50% 50%, rgba(255,255,255,.05), rgba(255,255,255,0) 70%);
  }
  .front-brand {
    position: absolute; left: 50%; top: 50%; transform: translate(-50%, -50%);
    display: flex; flex-direction: column; align-items: center;
  }
  .brand-row { display: flex; align-items: center; gap: 14px; }
  .brand-square { width: 30px; height: 30px; background: var(--white); }
  .brand-name {
    color: var(--cyan); font-weight: 900; font-size: 38px; letter-spacing: 1px; line-height: 1;
  }
  .brand-rule { width: 260px; height: 3px; background: var(--cyan); margin-top: 14px; }

  /* Back */
  .card-back { background: var(--paper); display: flex; }
  .contact-panel {
    width: 500px; background: linear-gradient(160deg, #173f69, var(--navy-deep));
    padding: 46px 0 0 52px; position: relative; color: var(--white);
  }
  .corner-tab {
    position: absolute; left: 0; bottom: 0; width: 0; height: 0;
    border-left: 46px solid var(--white); border-top: 46px solid transparent;
  }
  .person-name { font-size: 30px; font-weight: 700; line-height: 1.1; }
  .person-title { color: var(--cyan); font-size: 17px; margin-top: 4px; }
  .company { color: var(--cyan); font-size: 18px; margin-top: 20px; }
  .address { font-size: 16px; line-height: 1.35; margin-top: 2px; }
  .voip { color: var(--cyan); font-size: 15px; margin-top: 18px; }
  .voip b { color: var(--white); font-weight: 700; }
  .contact-list { list-style: none; margin-top: 6px; font-size: 16px; line-height: 1.45; }
  .contact-list li { display: flex; align-items: center; gap: 12px; }
  .contact-list svg { width: 14px; height: 14px; flex: none; }
  .contact-list .web b { font-weight: 900; }

  .logo-panel { flex: 1; display: flex; align-items: center; justify-content: center; background: var(--white); }
  .logo-box {
    width: 240px; height: 168px; background: var(--navy);
    display: flex; flex-direction: column; align-items: center; justify-content: center;
  }
  .logo-box .brand-square { width: 20px; height: 20px; }
  .logo-box .brand-name { font-size: 25px; }
  .logo-box .brand-rule { width: 170px; height: 2px; margin-top: 10px; }
</style>
</head>
<body>
  <section class="card card-front">
    <div class="map-texture" role="img" aria-label="Faint dotted world map texture"></div>
    <div class="front-brand">
      <div class="brand-row"><span class="brand-square"></span><span class="brand-name">TOVAR CREST</span></div>
      <div class="brand-rule"></div>
    </div>
  </section>

  <section class="card card-back">
    <div class="contact-panel">
      <h1 class="person-name">Carla Beth Soren</h1>
      <p class="person-title">VP, APAC M&amp;A Operations</p>
      <p class="company">Tovar Crest Asia Pacific Limited</p>
      <p class="address">Unit 1407, K82<br>27 Sai Lok Fung Road<br>Hong Kong</p>
      <p class="voip">VOIP: <b>4813</b></p>
      <ul class="contact-list">
        <li><svg viewBox="0 0 14 14"><rect x="3" y="1" width="8" height="12" rx="1.5" fill="none" stroke="#fff" stroke-width="1.4"/></svg>+852 6481 2037</li>
        <li><svg viewBox="0 0 14 14"><path d="M3 1l3 3-1.5 1.5a8 8 0 004 4L10 8l3 3-2 2C5 13 1 9 1 3z" fill="#fff"/></svg>+852 2736 4100</li>
        <li><svg viewBox="0 0 14 14"><rect x="1" y="5" width="12" height="8" fill="#fff"/><rect x="4" y="1" width="6" height="4" fill="none" stroke="#fff" stroke-width="1.4"/></svg>+852 2736 4155</li>
        <li><svg viewBox="0 0 14 14"><path d="M1 3h12v8H1z" fill="#fff"/><path d="M1 3l6 5 6-5" fill="none" stroke="#12365a" stroke-width="1.3"/></svg>cbsoren@tovarcrest.com</li>
        <li class="web"><svg viewBox="0 0 14 14"><circle cx="7" cy="7" r="6" fill="#fff"/><path d="M1 7h12M7 1c-3 3-3 9 0 12M7 1c3 3 3 9 0 12" fill="none" stroke="#12365a" stroke-width="1"/></svg>www.<b>tovarcrest</b>.com</li>
      </ul>
      <span class="corner-tab"></span>
    </div>
    <div class="logo-panel">
      <div class="logo-box">
        <div class="brand-row"><span class="brand-square"></span><span class="brand-name">TOVAR CREST</span></div>
        <div class="brand-rule"></div>
      </div>
    </div>
  </section>
</body>
</html>
```